Quillmere Business Advisory Business Card Design Project

I have a new business called Quillmere Business Advisory Limited. We provide business services for the UK for areas which include

Mentoring / Coaching
Interim Management
Non Executive Director / Chairman placement
Angel Investment support
Merger & Acquisition advice
Selling your business advice

I would like a background colour on the logo, a logo and our company name on the logo if possible.

I am open to colours but we want to portray a strong safe business with credibility

The business card design must match that of the logo design

Target Market(s)

SME and Medium size businesses with the owners, MD's, CEO or senior management as the target audiabce

Industry/Entity Type

Business

Requirements
Must have
• Match the logo design.
Look professional and quality
Should not have
• Old style text and colours
Poor logos depicting money

```html
<!DOCTYPE html>
<html lang="en">
<head>
<meta charset="utf-8">
<title>Quillmere Business Advisory – Business Card</title>
<link href="https://fonts.googleapis.com/css2?family=Cormorant+Garamond:wght@500;600&family=Tinos&family=Open+Sans:wght@400&display=swap" rel="stylesheet">
<style>
  :root {
    --backdrop: #e9e6e1;
    --card-white: #ffffff;
    --band-green: #a2dd0c;
    --accent-orange: #f07a18;
    --mark-green: #6cbf22;
    --ink: #1c1c1c;
  }
  * { margin: 0; padding: 0; box-sizing: border-box; }
  html, body {
    width: 1200px; height: 900px; overflow: hidden;
    background: var(--backdrop);
  }
  .card {
    position: absolute;
    left: 100px; top: 164px;
    width: 1000px; height: 572px;
    background: var(--card-white);
    box-shadow: 0 10px 30px rgba(0,0,0,0.18);
    overflow: hidden;
  }
  .brand-mark {
    position: absolute;
    left: 0; right: 0; top: 72px;
    display: flex; align-items: center; justify-content: center; gap: 18px;
  }
  .brand-mark__dot {
    width: 64px; height: 64px; border-radius: 50%;
    background: var(--mark-green);
  }
  .brand-mark__name {
    font-family: "Cormorant Garamond", Georgia, serif;
    font-weight: 600; font-size: 60px;
    color: var(--accent-orange);
  }
  .company-name {
    position: absolute;
    left: 0; right: 0; top: 214px;
    text-align: center;
    font-family: "Cormorant Garamond", Georgia, serif;
    font-weight: 500; font-size: 31px;
    letter-spacing: 0.5px;
    text-transform: uppercase;
    color: var(--ink);
  }
  .holder {
    position: absolute; left: 48px; top: 282px;
  }
  .holder__name {
    font-family: "Tinos", "Times New Roman", serif;
    font-size: 33px; color: var(--accent-orange);
    line-height: 1;
  }
  .holder__role {
    font-family: "Open Sans", Verdana, sans-serif;
    font-size: 20px; line-height: 26px; color: var(--ink);
    margin-top: 2px;
  }
  .contact-band {
    position: absolute;
    left: 0; right: 0; top: 352px; height: 198px;
    background: var(--band-green);
    padding: 34px 0 0 36px;
  }
  .contact-band p {
    font-family: "Open Sans", Verdana, sans-serif;
    font-size: 26px; line-height: 30px;
    color: var(--ink);
    letter-spacing: 0.6px;
  }
</style>
</head>
<body>
  <section class="card" aria-label="Quillmere Business Advisory business card">
    <div class="brand-mark">
      <span class="brand-mark__dot"></span>
      <span class="brand-mark__name">Quillmere</span>
    </div>
    <h1 class="company-name">Quillmere Business Advisory Limited</h1>
    <div class="holder">
      <div class="holder__name">Sample Name</div>
      <div class="holder__role">CEO</div>
    </div>
    <div class="contact-band">
      <p>2870 Harrow Lane, Suite 512</p>
      <p>Fairbridge, CA 90418</p>
      <p>Tel: 555-014-7731</p>
      <p>Cell: 555-019-2406</p>
      <p>Email: contact@quillmere.example</p>
    </div>
  </section>
</body>
</html>
```